Delcourt Realty Business Cards

Design business card

Target Market(s)

High-End Buyer of Real Estate over $1 million dollars

Industry/Entity Type

Realtor

Contact Information for Business Card

Lena Delcourt R(S) LIC.# 41972
Cell 555 246-1938
Email Lena@Delcourt.example
Website IsleFreshHomes.example

Also Need Cards for:

Hank Delcourt R(B) LIC# 69418
C 555 613-7052
E Hank@Delcourt.example
W IsleFreshHomes.example

Colors

Designer to choose colors to be used in the design.

Requirements
Must have
• Address on back:
• 287 Pohaku Cir. , Wailea HI 96753
• Logo on back
Nice to have
• I would like the phone numbers and email address to be big so people can read it easily
Should not have
• Very small print Except For: address (287 Pohaku Cir. Kalena HI 96799)

```html
<!DOCTYPE html>
<html lang="en">
<head>
<meta charset="utf-8">
<title>Delcourt Realty Business Cards</title>
<link href="https://fonts.googleapis.com/css2?family=Bebas+Neue&family=Josefin+Sans:wght@400;600&display=swap" rel="stylesheet">
<style>
  :root {
    --backdrop: #e9eaee;
    --slate: #2f343d;
    --logo-grey: #a7a9ac;
    --sky: #80d4ec;
    --white: #ffffff;
    --photo-light: #f4f4f4;
    --photo-warm: #c9a08a;
    --photo-dark: #2a2a2e;
  }
  * { box-sizing: border-box; margin: 0; padding: 0; }
  html, body { width: 1200px; height: 1200px; overflow: hidden; }
  body {
    background: var(--backdrop);
    font-family: "Josefin Sans", sans-serif;
    position: relative;
  }
  .card {
    position: absolute;
    left: 230px;
    width: 742px;
    height: 422px;
    overflow: hidden;
  }
  /* Front */
  .card-front { top: 137px; background: var(--photo-light); }
  .front-panel {
    position: absolute; left: 0; top: 0; width: 193px; height: 100%;
    background: var(--slate);
  }
  .front-logo {
    position: absolute; left: 47px; top: 120px; width: 100px;
    display: flex; flex-direction: column; align-items: center; gap: 14px;
  }
  .front-logo-mark {
    width: 56px; height: 56px; background: var(--logo-grey); border-radius: 6px;
  }
  .front-logo-name {
    color: var(--logo-grey); font-weight: 600; font-size: 15px;
    letter-spacing: 2px; text-align: center; line-height: 1.5;
  }
  .front-address {
    position: absolute; left: 0; width: 193px; top: 358px;
    color: var(--white); font-size: 14px; line-height: 25px; text-align: center;
    white-space: nowrap;
  }
  .agents-photo {
    position: absolute; left: 193px; top: 0; right: 0; bottom: 0;
    background: linear-gradient(100deg, var(--photo-light) 0%, var(--photo-light) 18%, var(--photo-warm) 40%, #b86a7a 55%, var(--photo-dark) 75%, var(--photo-light) 100%);
  }
  /* Back */
  .card-back { top: 638px; background: var(--sky); }
  .back-logo {
    position: absolute; left: 37px; top: 40px;
    display: flex; align-items: center; gap: 12px;
  }
  .back-logo-mark { width: 55px; height: 55px; background: var(--slate); border-radius: 6px; }
  .back-logo-name {
    color: var(--slate); font-weight: 600; font-size: 18px;
    letter-spacing: 2px; line-height: 1.25;
  }
  .agent-name {
    position: absolute; left: 40px;
    font-family: "Bebas Neue", sans-serif; font-weight: 400; font-size: 64px; line-height: 1;
    color: var(--slate); white-space: nowrap;
  }
  .agent-license {
    position: absolute; left: 40px;
    font-size: 20px; color: var(--white); letter-spacing: 1px; white-space: nowrap;
  }
  .name-lena { top: 158px; }
  .license-lena { top: 236px; }
  .name-hank { top: 283px; }
  .license-hank { top: 360px; }
  .contact {
    position: absolute; right: 165px; text-align: right;
    font-size: 16px; line-height: 24px; color: var(--slate); white-space: nowrap;
  }
  .contact-phones { top: 184px; }
  .contact-emails { top: 252px; }
  .contact-web { top: 336px; }
  .accent-line { position: absolute; left: 0; top: 0; }
  .icon-tab {
    position: absolute; left: 612px; width: 130px; height: 53px;
    background: var(--slate);
    display: flex; align-items: center; justify-content: center;
  }
  .tab-phone { top: 180px; }
  .tab-mail { top: 250px; }
  .tab-web { top: 320px; }
</style>
</head>
<body>
  <section class="card card-front">
    <div class="front-panel">
      <div class="front-logo">
        <div class="front-logo-mark"></div>
        <div class="front-logo-name">DELCOURT<br>REALTY</div>
      </div>
      <p class="front-address">287 Pohaku Cir.,<br>Kalena HI 96799</p>
    </div>
    <div class="agents-photo" role="img" aria-label="Portrait photo of agents Lena and Hank Delcourt against a white backdrop"></div>
  </section>

  <section class="card card-back">
    <div class="back-logo">
      <div class="back-logo-mark"></div>
      <div class="back-logo-name">DELCOURT<br>REALTY</div>
    </div>

    <svg class="accent-line" width="742" height="422" viewBox="0 0 742 422" aria-hidden="true">
      <rect x="711" y="42" width="8" height="16" fill="#ffffff"/>
      <rect x="711" y="75" width="8" height="15" fill="#ffffff"/>
      <rect x="711" y="115" width="8" height="307" fill="#ffffff"/>
    </svg>

    <h2 class="agent-name name-lena">Lena Delcourt</h2>
    <p class="agent-license license-lena">R(S) LIC.# 41972</p>
    <h2 class="agent-name name-hank">Hank Delcourt</h2>
    <p class="agent-license license-hank">R(B) LIC# 69418</p>

    <p class="contact contact-phones">555 246-1938<br>555 613-7052</p>
    <p class="contact contact-emails">Lena@Delcourt.example<br>Hank@Delcourt.example</p>
    <p class="contact contact-web">IsleFreshHomes.example</p>

    <div class="icon-tab tab-phone">
      <svg width="16" height="16" viewBox="0 0 16 16" aria-label="Phone"><rect x="4" y="1" width="8" height="14" rx="1.5" fill="#ffffff"/><rect x="6" y="3" width="4" height="8" fill="#2f343d"/></svg>
    </div>
    <div class="icon-tab tab-mail">
      <svg width="20" height="14" viewBox="0 0 20 14" aria-label="Email"><rect x="1" y="1" width="18" height="12" fill="none" stroke="#ffffff" stroke-width="1.6"/><path d="M1 1 L10 8 L19 1" fill="none" stroke="#ffffff" stroke-width="1.6"/></svg>
    </div>
    <div class="icon-tab tab-web">
      <svg width="16" height="16" viewBox="0 0 16 16" aria-label="Website"><circle cx="8" cy="8" r="7" fill="#ffffff"/><path d="M1 8 H15 M8 1 V15" stroke="#2f343d" stroke-width="1.2"/></svg>
    </div>
  </section>
</body>
</html>
```